Brookmere Osteopathy flyer

I want a clean clear DL flyer (but also want an A4 poster) promoting a new Osteopathic business in a semi rural area in Tasmania (Australia).
It can have pictures like the examples attached to show people what Osteopathy is (its like Chiropractic and physiotherapy).
I am the sole practioner and am male, so any pictures would be best to be a white male if possible.
I've attached some wording, you can use all, or none of it
I don't have a phone number for the business yet
info@brookmereosteopathy.example
www.brookmereosteopathy.example
Target Market(s)
Australians, from tradies, professionals, babies to retired people
Industry/Entity Type
Health
Look and feel

```html
<!DOCTYPE html>
<html lang="en">
<head>
<meta charset="utf-8">
<title>Brookmere Osteopathy – DL Flyer</title>
<link rel="stylesheet" href="https://fonts.googleapis.com/css2?family=Roboto:ital,wght@0,400;0,500;0,700;1,400&display=swap">
<style>
  :root{
    --blue:#0b96d1;
    --blue-light:#4aaedb;
    --orange:#f0801f;
    --orange-light:#f7953a;
    --ink:#1d1d1b;
    --white:#ffffff;
    --backdrop:#d9d9dc;
  }
  *{margin:0;padding:0;box-sizing:border-box}
  html,body{width:1200px;height:1068px;overflow:hidden}
  body{background:var(--backdrop);font-family:"Roboto",Arial,sans-serif;color:var(--ink);position:relative}
  .flyer{position:absolute;top:147px;width:378px;height:755px;background:var(--white);overflow:hidden;box-shadow:0 6px 18px rgba(0,0,0,.18)}
  .flyer--front{left:161px}
  .flyer--back{left:660px}
  .flyer__art{position:absolute;inset:0;width:378px;height:755px}
  .photo{position:absolute}

  /* front */
  .brand{position:absolute;top:26px;left:0;width:378px;text-align:center}
  .brand__mark{display:block;width:44px;height:44px;margin:0 auto 10px;border:3px solid var(--blue);border-radius:50%}
  .brand__name{font-weight:700;font-size:17px;color:var(--blue);letter-spacing:.5px}
  .contact-band{position:absolute;top:436px;left:0;width:378px;display:flex;align-items:center;justify-content:center;gap:10px;color:var(--white);font-weight:500;font-size:18px}
  .contact-band svg{flex:none}
  .web{position:absolute;top:710px;left:0;width:378px;text-align:center;color:var(--white);font-style:italic;font-size:20px}

  /* back */
  .reasons{position:absolute;top:20px;left:23px}
  .reasons__title{color:var(--orange);font-weight:700;font-size:17px;line-height:21px}
  .reasons__list{list-style:none;margin-top:8px}
  .reasons__list li{position:relative;padding-left:21px;font-size:14.2px;line-height:18.2px}
  .reasons__list li::before{content:"";position:absolute;left:2px;top:6px;width:6px;height:6px;border-radius:50%;background:var(--blue)}
  .badge{position:absolute;left:236px;top:27px;width:104px;height:104px;border-radius:50%;background:var(--white);border:3px solid var(--blue);display:flex;align-items:center;justify-content:center;text-align:center;color:var(--blue);font-weight:700;font-size:12px;line-height:15px}
  .method{position:absolute;top:276px;left:19px;width:275px;color:var(--white);font-size:18px;line-height:21.8px}
  .method__lead{font-weight:700;font-size:21.5px}
  .method strong{font-weight:700;font-size:19px}
  .contact{position:absolute;top:484px;left:23px;font-size:16.4px;line-height:20px}
  .contact__row{display:flex;align-items:flex-start;gap:9px}
  .contact__row svg{flex:none}
  .contact__row--email{margin-top:8px;font-size:13px;align-items:center}
</style>
</head>
<body>

<section class="flyer flyer--front">
  <svg class="flyer__art" viewBox="0 0 378 755" aria-hidden="true">
    <defs>
      <linearGradient id="frontFade" x1="0" y1="0" x2="0" y2="1">
        <stop offset="0" stop-color="#ffffff"/>
        <stop offset=".22" stop-color="#f1e4d9" stop-opacity="0"/>
      </linearGradient>
      <linearGradient id="frontPhoto" x1="0" y1="0" x2="1" y2="1">
        <stop offset="0" stop-color="#e8d3c0"/>
        <stop offset=".35" stop-color="#d79a74"/>
        <stop offset=".6" stop-color="#c98663"/>
        <stop offset=".8" stop-color="#5a4538"/>
        <stop offset="1" stop-color="#2f2824"/>
      </linearGradient>
      <radialGradient id="thumbA" cx=".5" cy=".5" r=".6">
        <stop offset="0" stop-color="#d6ad95"/>
        <stop offset=".5" stop-color="#5b4c45"/>
        <stop offset="1" stop-color="#e7e8ea"/>
      </radialGradient>
      <radialGradient id="thumbB" cx=".5" cy=".4" r=".6">
        <stop offset="0" stop-color="#e2b8a3"/>
        <stop offset=".55" stop-color="#5f93b7"/>
        <stop offset="1" stop-color="#9aa6b4"/>
      </radialGradient>
      <radialGradient id="thumbC" cx=".5" cy=".55" r=".6">
        <stop offset="0" stop-color="#caa08a"/>
        <stop offset=".5" stop-color="#4f443f"/>
        <stop offset="1" stop-color="#eef0f2"/>
      </radialGradient>
    </defs>
    <rect x="0" y="120" width="378" height="300" fill="url(#frontPhoto)"/>
    <rect x="0" y="120" width="378" height="300" fill="url(#frontFade)"/>
    <path d="M0,372 C110,395 260,410 378,366 L378,760 L0,760 Z" fill="var(--orange)"/>
    <path d="M0,386 C110,420 270,428 378,378 L378,760 L0,760 Z" fill="var(--blue)" stroke="var(--white)" stroke-width="2.5"/>
    <path d="M0,552 C60,500 120,478 200,500 C260,515 320,522 378,495 L378,592 L0,592 Z" fill="var(--orange-light)" stroke="var(--white)" stroke-width="2.5"/>
    <path d="M0,590 L378,590 L378,760 L0,760 Z" fill="var(--white)"/>
    <path d="M0,668 Q189,742 378,668 L378,755 L0,755 Z" fill="var(--blue-light)"/>
    <circle cx="67" cy="607" r="54" fill="url(#thumbA)" stroke="var(--orange-light)" stroke-width="4"/>
    <circle cx="190" cy="607" r="54" fill="url(#thumbB)" stroke="var(--orange-light)" stroke-width="4"/>
    <circle cx="312" cy="607" r="54" fill="url(#thumbC)" stroke="var(--orange-light)" stroke-width="4"/>
  </svg>
  <div class="photo" role="img" aria-label="Practitioner cradling a relaxed patient's head and neck during treatment" style="left:0;top:130px;width:378px;height:240px"></div>
  <div class="photo" role="img" aria-label="Shoulder mobilisation treatment" style="left:13px;top:553px;width:108px;height:108px;border-radius:50%"></div>
  <div class="photo" role="img" aria-label="Gentle treatment of a baby" style="left:136px;top:553px;width:108px;height:108px;border-radius:50%"></div>
  <div class="photo" role="img" aria-label="Lower back treatment" style="left:258px;top:553px;width:108px;height:108px;border-radius:50%"></div>

  <div class="brand">
    <span class="brand__mark"></span>
    <span class="brand__name">Brookmere Osteopathy</span>
  </div>

  <div class="contact-band">
    <svg width="22" height="15" viewBox="0 0 16 11" aria-hidden="true"><rect x="0" y="0" width="16" height="11" rx="1" fill="var(--orange-light)"/><path d="M0.5 0.8 L8 6.5 L15.5 0.8" fill="none" stroke="var(--blue)" stroke-width="1.2"/></svg>
    <span>info@brookmereosteopathy.example</span>
  </div>

  <p class="web">www.brookmereosteopathy.example</p>
</section>

<section class="flyer flyer--back">
  <svg class="flyer__art" viewBox="0 0 378 755" aria-hidden="true">
    <defs>
      <linearGradient id="backFade" x1="0" y1="0" x2="0" y2="1">
        <stop offset="0" stop-color="#ffffff"/>
        <stop offset=".3" stop-color="#ffffff" stop-opacity="0"/>
      </linearGradient>
      <radialGradient id="backPhoto" cx=".55" cy=".7" r=".7">
        <stop offset="0" stop-color="#3a2c27"/>
        <stop offset=".25" stop-color="#c99a86"/>
        <stop offset=".6" stop-color="#edd2c4"/>
        <stop offset="1" stop-color="#f6ebe5"/>
      </radialGradient>
    </defs>
    <rect x="0" y="540" width="300" height="215" fill="url(#backPhoto)"/>
    <rect x="0" y="540" width="300" height="215" fill="url(#backFade)"/>
    <path d="M0,265 L300,265 L290,465 L0,465 Z" fill="var(--blue)"/>
    <path d="M243,0 C262,60 302,120 300,260 C298,420 262,560 284,755 L378,755 L378,0 Z" fill="var(--blue-light)" stroke="var(--white)" stroke-width="4"/>
    <path d="M250,0 C270,60 310,120 308,260 C306,420 272,560 294,755 L378,755 L378,0 Z" fill="var(--blue)"/>
    <path d="M357,0 C352,200 342,500 366,755 L378,755 L378,0 Z" fill="var(--orange)" stroke="var(--white)" stroke-width="2.5"/>
    <path d="M364,0 C360,200 352,500 372,755 L378,755 L378,0 Z" fill="var(--orange-light)"/>
  </svg>
  <div class="photo" role="img" aria-label="Hands resting on a patient's forehead during a calming head treatment" style="left:0;top:560px;width:290px;height:195px"></div>

  <div class="reasons">
    <h2 class="reasons__title">Common reasons people<br>visit an osteopath:</h2>
    <ul class="reasons__list">
      <li>Back / neck pain</li>
      <li>Headaches / migraines</li>
      <li>Joint and muscle pain</li>
      <li>Pregnancy-related discomfort</li>
      <li>Disc related issues</li>
      <li>Sciatica</li>
      <li>Plantar fasciitis</li>
      <li>Tendonitis / Bursitis</li>
      <li>Adhesive capsulitis (frozen shoulder)</li>
      <li>Tennis / Golfers elbow</li>
    </ul>
  </div>

  <div class="badge">Brookmere<br>Osteopathy</div>

  <p class="method">
    <span class="method__lead">Osteopaths</span> use a<br>
    combination of<br>
    <strong>joint manipulation, targeted<br>deep tissue massage<br>and stretching</strong><br>
    to improve function, relieve<br>pain and support the body’s<br>ability to heal itself.
  </p>

  <div class="contact">
    <div class="contact__row">
      <svg width="16" height="22" viewBox="0 0 16 22" aria-hidden="true"><path fill="var(--blue)" d="M8 0C3.6 0 0 3.5 0 7.9 0 13.6 8 22 8 22s8-8.4 8-14.1C16 3.5 12.4 0 8 0zm0 11a3.2 3.2 0 1 1 0-6.4A3.2 3.2 0 0 1 8 11z"/></svg>
      <span>24 Willow Creek road<br>Brookmere</span>
    </div>
    <div class="contact__row contact__row--email">
      <svg width="16" height="11" viewBox="0 0 16 11" aria-hidden="true"><rect x="0" y="0" width="16" height="11" fill="var(--blue)"/><path d="M0.5 0.8 L8 6.5 L15.5 0.8" fill="none" stroke="var(--white)" stroke-width="1.2"/></svg>
      <span>info@brookmereosteopathy.example</span>
    </div>
  </div>
</section>

</body>
</html>
```